Letterhead & Visiting Cards for Outdoor cleaning company
Talvex
Letterhead & Visiting Cards for Outdoor cleaning company - Cleaning
Creative Brief
Professional
Kiran Mehtolkar
B7, Vrundavan, Plot No. 52, Rane Path Colony, Borvali (West), Mumbai 400163
kiran@talvex.co.in
talvex.co.in
Logo with AI files and fonts is placed at http://talvex.brimsoft.net/talvex_logos.zip
The service list should be displayed on the back of the card. The list of services can be obtained from the website.

```html
<!DOCTYPE html>
<html lang="en">
<head>
<meta charset="utf-8">
<title>Talvex Visiting Cards</title>
<link rel="stylesheet" href="https://fonts.googleapis.com/css2?family=Ubuntu:wght@400;500;700&family=Open+Sans:wght@400;600&display=swap">
<style>
  :root {
    --bg: #2a2a2c;
    --blue-deep: #2b2f8f;
    --blue-mid: #2447a8;
    --blue-light: #3c7fd0;
    --green-deep: #1d7a34;
    --green-mid: #2f9a3c;
    --green-light: #8cc63f;
    --brand-green: #2e8b3a;
    --white: #ffffff;
  }
  * { margin: 0; padding: 0; box-sizing: border-box; }
  html, body { width: 1200px; height: 871px; overflow: hidden; }
  body {
    background: var(--bg);
    position: relative;
    font-family: "Open Sans", sans-serif;
  }
  .card {
    position: absolute;
    top: 280px;
    width: 540px;
    height: 310px;
    border-radius: 18px;
    overflow: hidden;
  }
  .card-back {
    left: 40px;
    background: linear-gradient(135deg, var(--blue-deep) 0%, var(--blue-mid) 55%, var(--blue-light) 100%);
  }
  .back-figure {
    position: absolute;
    left: 220px;
    top: 40px;
    width: 100px;
    height: 140px;
    border-radius: 10px;
    background: linear-gradient(180deg, rgba(210,225,255,0.85), rgba(160,185,235,0.55));
  }
  .back-rule {
    position: absolute;
    left: 100px;
    top: 200px;
    width: 340px;
    height: 1px;
    background: rgba(255,255,255,0.6);
  }
  .service-list {
    position: absolute;
    left: 0;
    top: 218px;
    width: 100%;
    text-align: center;
    color: var(--white);
    font-size: 13px;
    line-height: 20px;
  }
  .card-front {
    left: 620px;
    background: var(--white);
  }
  .card-front svg.front-art {
    position: absolute;
    inset: 0;
  }
  .brand-name {
    position: absolute;
    left: 30px;
    top: 34px;
    font-family: "Ubuntu", sans-serif;
    font-weight: 700;
    font-size: 46px;
    letter-spacing: 1px;
    color: var(--brand-green);
    display: flex;
    align-items: center;
    gap: 12px;
  }
  .brand-mark {
    width: 14px;
    height: 14px;
    background: var(--blue-mid);
    border-radius: 50%;
  }
  .person-name {
    position: absolute;
    right: 34px;
    top: 108px;
    font-family: "Ubuntu", sans-serif;
    font-weight: 700;
    font-size: 19px;
    color: var(--brand-green);
  }
  .contact-list {
    position: absolute;
    right: 30px;
    top: 196px;
    list-style: none;
    text-align: right;
    color: var(--white);
    font-size: 13px;
    line-height: 18px;
  }
  .contact-list li { display: flex; justify-content: flex-end; align-items: center; gap: 8px; }
  .contact-list svg { width: 12px; height: 12px; flex: none; }
  .contact-list .no-icon { padding-right: 20px; }
</style>
</head>
<body>

<section class="card card-back">
  <div class="back-figure" role="img" aria-label="Silhouette of a cleaning worker with a pressure washer"></div>
  <div class="back-rule"></div>
  <p class="service-list">
    Lawn care · Facade washing · Pressure cleaning<br>
    Gutter clearing · Paving restoration · Patios
  </p>
</section>

<section class="card card-front">
  <svg class="front-art" width="540" height="310" viewBox="0 0 540 310">
    <defs>
      <linearGradient id="greenFill" x1="0" y1="0" x2="1" y2="0">
        <stop offset="0" stop-color="#1f7f35"/>
        <stop offset="0.45" stop-color="#6fb83f"/>
        <stop offset="1" stop-color="#1d7a34"/>
      </linearGradient>
    </defs>
    <path d="M0,212 C120,178 220,236 330,212 C420,192 480,178 540,184 L540,310 L0,310 Z" fill="url(#greenFill)"/>
    <path d="M0,196 C120,168 220,226 330,200 C420,180 480,170 540,176" fill="none" stroke="#8cc63f" stroke-width="4"/>
    <path d="M0,160 C90,196 200,214 300,192 C400,170 470,156 540,164 L540,180 C470,174 400,186 300,206 C200,226 90,212 0,176 Z" fill="#2447a8"/>
  </svg>

  <div class="brand-name">TALVEX <span class="brand-mark"></span></div>
  <p class="person-name">Kiran Mehtolkar</p>

  <ul class="contact-list">
    <li>+91-22-27418302
      <svg viewBox="0 0 12 12"><path d="M2 1h3l1 3-2 1a7 7 0 0 0 3 3l1-2 3 1v3a1 1 0 0 1-1 1A10 10 0 0 1 1 2a1 1 0 0 1 1-1z" fill="#fff"/></svg>
    </li>
    <li>9823401957
      <svg viewBox="0 0 12 12"><rect x="3" y="0.5" width="6" height="11" rx="1" fill="none" stroke="#fff"/><circle cx="6" cy="9.5" r="0.7" fill="#fff"/></svg>
    </li>
    <li>kiran@talvex.co.in
      <svg viewBox="0 0 12 12"><rect x="0.5" y="2.5" width="11" height="7" fill="none" stroke="#fff"/><path d="M0.5 2.5 6 7l5.5-4.5" fill="none" stroke="#fff"/></svg>
    </li>
    <li>www.talvex.co.in
      <svg viewBox="0 0 12 12"><circle cx="6" cy="6" r="5.3" fill="none" stroke="#fff"/><ellipse cx="6" cy="6" rx="2.3" ry="5.3" fill="none" stroke="#fff"/><path d="M0.7 6h10.6" stroke="#fff"/></svg>
    </li>
    <li class="no-icon">B7, Vrundavan, Plot No. 52, Rane Path Colony,</li>
    <li class="no-icon">Borvali (West), Mumbai 400163</li>
  </ul>
</section>

</body>
</html>
```